High-end construction company needs a business card design

We need a modern looking business card that draws people in, is memorable and looks so good people will want to sick it on their fridges.
On the first side what is needed are:
Logo
My name - Tomas Verbelk
Title - Managing Director
Website - www.kravel.co.uk
Email - tomas@kravel.co.uk
Telephone - 020 5194 6381
Mobile - 07845319027
On the back side was is needed is a list of all the services we provide:
-Kitchen Renovations
-Bathroom Renovations
-House Renovations
-Garage Conversions
-Extensions
-Loft Conversions
-Conservatories
-Carpentry
-Tiling
-Electrical
-Plumbing & Heating
-Bricklaying
-Landscaping
-Decorating
-Plastering
We would like the colours to be the same shades as on the logo with grey or black for the words.
Target Market(s)
Anyone who needs building work done
Contact Information for Business Card
This business card is for a construction company which strives to deliver excellent service and quality.
The look and feel of the card should represent this.
Requirements
Must have
- On the first side what is needed are:
Logo
My name - Tomas Verbelk
Title - Managing Director
Website - www.kravel.co.uk
Email - tomas@kravel.co.uk
Telephone - 020 5194 6381
Mobile - 07845319027
Nice to have
- Cool looking features

```html
<!DOCTYPE html>
<html lang="en">
<head>
<meta charset="utf-8">
<title>Kravel Construction – Business Card</title>
<link rel="stylesheet" href="https://fonts.googleapis.com/css2?family=Didact+Gothic&family=Oswald:wght@700&display=swap">
<style>
  :root {
    --backdrop: #5e5e60;
    --card-grey: #a7a7a8;
    --card-white: #ffffff;
    --brand-green: #18b446;
    --text-light: #ffffff;
    --shadow: rgba(0,0,0,0.35);
  }
  * { box-sizing: border-box; margin: 0; padding: 0; }
  html, body { width: 1200px; height: 1200px; overflow: hidden; }
  body {
    background: var(--backdrop);
    font-family: "Didact Gothic", "Century Gothic", sans-serif;
    color: var(--text-light);
    position: relative;
  }
  .card {
    position: absolute;
    left: 150px;
    width: 900px;
    height: 514px;
    overflow: hidden;
    box-shadow: 0 10px 28px var(--shadow);
  }
  .card--services { top: 60px; background: var(--card-grey); }
  .card--contact { top: 626px; background: var(--card-grey); }

  .hazard-band {
    position: absolute;
    left: -20px; right: -20px; bottom: 0;
    height: 30px;
    background: repeating-linear-gradient(90deg, var(--brand-green) 0 46px, transparent 46px 96px);
    transform: skewX(-35deg);
  }

  /* Services side */
  .services-title {
    position: absolute;
    left: 60px; top: 92px;
    font-family: "Oswald", "Arial Narrow", sans-serif;
    font-weight: 700;
    font-size: 50px;
    letter-spacing: 1px;
    color: var(--brand-green);
    line-height: 1;
  }
  .services-list {
    position: absolute;
    top: 162px;
    list-style: none;
    font-size: 31px;
    line-height: 43px;
  }
  .services-list li::before {
    content: "•";
    margin-right: 12px;
  }
  .services-list--left { left: 66px; }
  .services-list--right { left: 480px; top: 98px; }
  .machine-art {
    position: absolute;
    right: 30px; top: 24px;
    width: 190px; height: 84px;
    background: linear-gradient(135deg, rgba(24,180,70,0.9), rgba(24,180,70,0.55));
    border-radius: 6px;
  }

  /* Contact side */
  .contact-panel {
    position: absolute;
    left: 0; top: 0; bottom: 0;
    width: 500px;
    padding: 48px 0 0 44px;
  }
  .person-name { font-size: 52px; line-height: 1.1; }
  .person-title { font-size: 28px; margin: 4px 0 38px 58px; }
  .contact-list { list-style: none; }
  .contact-list li {
    display: flex;
    align-items: center;
    gap: 14px;
    font-size: 33px;
    height: 58px;
  }
  .contact-icon {
    width: 44px; height: 44px;
    border-radius: 50%;
    background: var(--card-white);
    display: flex; align-items: center; justify-content: center;
    flex: none;
  }
  .contact-icon svg { width: 26px; height: 26px; }
  .brand-panel {
    position: absolute;
    left: 500px; top: 0; right: 0; bottom: 0;
    background: var(--card-white);
    display: flex;
    flex-direction: column;
    align-items: center;
    justify-content: center;
    padding-bottom: 40px;
  }
  .brand-mark {
    display: flex;
    align-items: center;
    gap: 14px;
    color: var(--brand-green);
    font-size: 62px;
    letter-spacing: 4px;
  }
  .brand-mark__square {
    width: 40px; height: 40px;
    background: var(--brand-green);
  }
  .brand-sub {
    color: var(--brand-green);
    font-size: 20px;
    letter-spacing: 3px;
    margin-top: 6px;
  }
  .card--contact .hazard-band { z-index: 2; }
</style>
</head>
<body>

  <section class="card card--services" aria-label="Services side">
    <div class="machine-art" role="img" aria-label="Green excavator arm illustration"></div>
    <h2 class="services-title">OUR SERVICES</h2>
    <ul class="services-list services-list--left">
      <li>House Renovations</li>
      <li>Kitchen Renovations</li>
      <li>Bathroom Renovations</li>
      <li>Garage Conversions</li>
      <li>Extensions</li>
      <li>Loft Conversions</li>
      <li>Conservatories</li>
    </ul>
    <ul class="services-list services-list--right">
      <li>Carpentry</li>
      <li>Electrical</li>
      <li>Plumbing &amp; Heating</li>
      <li>Bricklaying</li>
      <li>Landscaping</li>
      <li>Decorating</li>
      <li>Plastering</li>
    </ul>
    <div class="hazard-band"></div>
  </section>

  <section class="card card--contact" aria-label="Contact side">
    <div class="contact-panel">
      <h1 class="person-name">Tomas Verbelk</h1>
      <p class="person-title">Managing Director</p>
      <ul class="contact-list">
        <li>
          <span class="contact-icon">
            <svg viewBox="0 0 24 24" fill="none" stroke="#18b446" stroke-width="2">
              <circle cx="12" cy="12" r="10"/><ellipse cx="12" cy="12" rx="4.5" ry="10"/><line x1="2" y1="12" x2="22" y2="12"/><line x1="4" y1="7" x2="20" y2="7"/><line x1="4" y1="17" x2="20" y2="17"/>
            </svg>
          </span>www.kravel.co.uk
        </li>
        <li>
          <span class="contact-icon">
            <svg viewBox="0 0 24 24" fill="none" stroke="#18b446" stroke-width="2">
              <rect x="2" y="5" width="20" height="14"/><polyline points="2,5 12,13 22,5"/>
            </svg>
          </span>tomas@kravel.co.uk
        </li>
        <li>
          <span class="contact-icon">
            <svg viewBox="0 0 24 24" fill="#18b446">
              <path d="M6.6 10.8a15 15 0 0 0 6.6 6.6l2.2-2.2a1 1 0 0 1 1-.25 11.4 11.4 0 0 0 3.6.57 1 1 0 0 1 1 1V20a1 1 0 0 1-1 1A17 17 0 0 1 3 4a1 1 0 0 1 1-1h3.5a1 1 0 0 1 1 1c0 1.25.2 2.45.57 3.6a1 1 0 0 1-.25 1z"/>
            </svg>
          </span>020 5194 6381
        </li>
        <li>
          <span class="contact-icon">
            <svg viewBox="0 0 24 24" fill="none" stroke="#18b446" stroke-width="2">
              <rect x="6" y="2" width="12" height="20" rx="2"/><line x1="11" y1="18" x2="13" y2="18"/>
            </svg>
          </span>07845319027
        </li>
      </ul>
    </div>
    <div class="brand-panel">
      <div class="brand-mark"><span class="brand-mark__square"></span>KRAVEL</div>
      <div class="brand-sub">CONSTRUCTION LTD</div>
    </div>
    <div class="hazard-band"></div>
  </section>

</body>
</html>
```